Brennick Works 'Velvet Glaze' Label

We need a label for our new Exterior Ceramic Coat spray. It is going to be called Velvet Glaze. This label needs to exude a premium feel yet also retain elements of FUN. This product when applied to a vehicle exterior creates a highly durable barrier and incredible shine. Ceramic coats are a popular way to make your paint turn heads! - and ours is the best. We'd like to see designs that match our line and previous projects but we want this label to stick out a little like its something special. Oranges, Reds, Silver, White, could all be great ideas, we dont have a set color or fragrance for this yet so all ideas are welcome!

```html
<!DOCTYPE html>
<html lang="en">
<head>
<meta charset="utf-8">
<title>Brennick Works – Velvet Glaze Label</title>
<link href="https://fonts.googleapis.com/css2?family=Russo+One&family=Montserrat:wght@500;700;800&family=Oswald:wght@400;500&display=swap" rel="stylesheet">
<style>
  :root {
    --page: #f2f2f2;
    --label-white: #ffffff;
    --pattern-light: #f7f7f7;
    --pattern-mid: #e2e2e2;
    --pattern-dark: #cfcfcf;
    --red: #e01e26;
    --deep-red: #b5121b;
    --grey-band: #c9c9c9;
    --ink: #1a1a1a;
    --black: #111111;
    --silver-light: #f4f4f4;
    --silver-mid: #bdbdbd;
    --silver-dark: #7d7d7d;
  }
  html, body {
    margin: 0;
    width: 1200px;
    height: 1200px;
    overflow: hidden;
    background: var(--page);
  }
  .canvas {
    position: relative;
    width: 1200px;
    height: 1200px;
  }
  .label {
    position: absolute;
    left: 270px;
    top: 185px;
    width: 660px;
    height: 830px;
    border-radius: 90px 90px 24px 24px;
    overflow: hidden;
    background: var(--label-white);
    box-shadow: 0 10px 30px rgba(0,0,0,0.12);
  }
  .label-texture {
    position: absolute;
    inset: 0;
    background:
      radial-gradient(ellipse at 30% 25%, var(--label-white) 0%, rgba(255,255,255,0) 60%),
      linear-gradient(160deg, var(--pattern-light) 0%, var(--pattern-mid) 55%, var(--pattern-dark) 100%);
  }
  .brand {
    position: absolute;
    top: 130px;
    left: 0;
    width: 100%;
    display: flex;
    justify-content: center;
    align-items: center;
    gap: 16px;
  }
  .brand-mark {
    width: 30px;
    height: 30px;
    background: var(--deep-red);
  }
  .brand-name {
    font-family: "Montserrat", sans-serif;
    font-weight: 800;
    font-size: 50px;
    color: var(--ink);
    letter-spacing: 1px;
  }
  .product-name {
    position: absolute;
    left: 55px;
    top: 285px;
    margin: 0;
    font-family: "Russo One", sans-serif;
    font-weight: 400;
    font-size: 84px;
    line-height: 86px;
    color: var(--deep-red);
    text-transform: uppercase;
    letter-spacing: 5px;
  }
  .gem-art {
    position: absolute;
    left: 440px;
    top: 395px;
    width: 195px;
    height: 215px;
    border-radius: 14px;
    background: linear-gradient(150deg, var(--silver-light), var(--silver-mid) 55%, var(--silver-dark));
  }
  .tagline {
    position: absolute;
    left: 0;
    top: 495px;
    width: 470px;
    height: 38px;
    background: var(--red);
    clip-path: polygon(0 0, 100% 0, 94% 100%, 0 100%);
    font-family: "Montserrat", sans-serif;
    font-weight: 700;
    font-size: 27px;
    line-height: 38px;
    color: var(--label-white);
    padding-left: 55px;
    box-sizing: border-box;
  }
  .benefit-band {
    position: absolute;
    left: 0;
    top: 540px;
    width: 470px;
    height: 38px;
    background: var(--grey-band);
    clip-path: polygon(0 0, 94% 0, 100% 100%, 0 100%);
    font-family: "Montserrat", sans-serif;
    font-weight: 500;
    font-size: 25px;
    line-height: 38px;
    color: #333;
    letter-spacing: 1px;
    padding-left: 55px;
    box-sizing: border-box;
  }
  .feature-band {
    position: absolute;
    left: 0;
    top: 615px;
    width: 100%;
    height: 215px;
    background: var(--red);
  }
  .features {
    position: absolute;
    left: 40px;
    top: 20px;
    display: flex;
    gap: 20px;
  }
  .feature {
    width: 112px;
    text-align: center;
  }
  .feature-icon {
    width: 96px;
    height: 96px;
    margin: 0 auto;
    border-radius: 50%;
    background: var(--label-white);
    display: flex;
    align-items: center;
    justify-content: center;
  }
  .feature-caption {
    margin-top: 10px;
    font-family: "Oswald", sans-serif;
    font-size: 18px;
    line-height: 21px;
    color: var(--label-white);
  }
  .volume-corner {
    position: absolute;
    right: 0;
    bottom: 0;
    width: 240px;
    height: 215px;
    background: var(--black);
    clip-path: polygon(100% 0, 100% 100%, 0 100%);
  }
  .volume {
    position: absolute;
    right: 40px;
    bottom: 35px;
    text-align: center;
    font-family: "Oswald", sans-serif;
    color: var(--label-white);
  }
  .volume-number {
    font-size: 54px;
    line-height: 56px;
  }
  .volume-unit {
    font-size: 26px;
    line-height: 30px;
  }
</style>
</head>
<body>
<div class="canvas">
  <div class="label">
    <div class="label-texture" role="img" aria-label="Quilted white and silver background texture"></div>

    <div class="brand">
      <span class="brand-mark"></span>
      <span class="brand-name">Brennick Works</span>
    </div>

    <h1 class="product-name">Velvet<br>Glaze</h1>

    <div class="gem-art" role="img" aria-label="Silver gemstone illustration"></div>

    <div class="tagline">Exterior Ceramic Coat</div>
    <div class="benefit-band">HIGHLY DURABLE BARRIER</div>

    <div class="feature-band">
      <div class="features">
        <div class="feature">
          <div class="feature-icon">
            <svg width="54" height="60" viewBox="0 0 54 60" aria-hidden="true">
              <path d="M27 2 L50 10 V28 C50 44 40 53 27 58 C14 53 4 44 4 28 V10 Z" fill="#111"/>
              <circle cx="36" cy="40" r="9" fill="#e01e26"/>
            </svg>
          </div>
          <div class="feature-caption">Highly Durable<br>Barrier</div>
        </div>
        <div class="feature">
          <div class="feature-icon">
            <svg width="60" height="60" viewBox="0 0 60 60" aria-hidden="true">
              <path d="M30 4 L35 25 L56 30 L35 35 L30 56 L25 35 L4 30 L25 25 Z" fill="#111"/>
              <circle cx="48" cy="12" r="4" fill="#e01e26"/>
            </svg>
          </div>
          <div class="feature-caption">Incredible<br>Shine</div>
        </div>
        <div class="feature">
          <div class="feature-icon">
            <svg width="60" height="60" viewBox="0 0 60 60" aria-hidden="true">
              <circle cx="30" cy="34" r="10" fill="#111"/>
              <circle cx="30" cy="34" r="19" fill="none" stroke="#111" stroke-width="4"/>
              <path d="M30 4 V10 M12 10 L16 15 M48 10 L44 15" stroke="#e01e26" stroke-width="4" stroke-linecap="round"/>
            </svg>
          </div>
          <div class="feature-caption">Easy to<br>Use</div>
        </div>
      </div>
      <div class="volume-corner"></div>
      <div class="volume">
        <div class="volume-number">16</div>
        <div class="volume-unit">FL. OZ.</div>
      </div>
    </div>
  </div>
</div>
</body>
</html>
```